KORBALT

The business want a professional looking business card. We have a scetch we will add but want the extra upgrade, and would like more suggestions for variations of our business cards.

```html
<!DOCTYPE html>
<html lang="en">
<head>
<meta charset="utf-8">
<title>KORBALT – Business Card</title>
<link rel="stylesheet" href="https://fonts.googleapis.com/css2?family=Marcellus&family=Montserrat:wght@600;700;800&family=Open+Sans:wght@600&display=swap">
<style>
  :root {
    --backdrop: #202020;
    --gold-light: #f3d588;
    --gold-mid: #d2a85a;
    --gold-deep: #b3832f;
    --ink-brown: #7b4a22;
    --ink-soft: #93612f;
    --cream: #fbf1c4;
    --wordmark-gold: #f0b650;
  }
  * { margin: 0; padding: 0; box-sizing: border-box; }
  html, body { width: 850px; height: 1200px; overflow: hidden; background: var(--backdrop); }
  .canvas { position: relative; width: 850px; height: 1200px; }

  .card {
    position: absolute;
    left: 134px;
    width: 582px;
    height: 377px;
    border-radius: 21px;
    overflow: hidden;
    background:
      repeating-linear-gradient(0deg, rgba(255,255,255,0.05) 0 1px, rgba(0,0,0,0.035) 1px 2px, transparent 2px 3px),
      linear-gradient(120deg, var(--gold-light) 0%, var(--gold-mid) 45%, var(--gold-deep) 100%);
  }
  .card--front { top: 139px; }
  .card--back { top: 630px; }

  .company-name {
    position: absolute; left: 54px; top: 62px;
    font: 400 29px/1 "Marcellus", serif;
    color: var(--ink-brown);
    letter-spacing: 0.5px;
  }
  .job-title {
    position: absolute; left: 55px; top: 106px;
    font: 600 26px/1 "Montserrat", sans-serif;
    color: var(--ink-brown);
  }
  .person-name {
    position: absolute; left: 55px; top: 135px;
    font: 600 15.5px/1 "Montserrat", sans-serif;
    color: var(--ink-brown);
  }
  .contact-list { position: absolute; left: 57px; top: 236px; list-style: none; }
  .contact-item {
    display: flex; align-items: center; height: 27px;
    font: 600 16px/1 "Open Sans", sans-serif;
    color: var(--ink-soft);
  }
  .contact-icon { width: 14px; height: 14px; margin-right: 12px; fill: var(--ink-brown); }

  .front-brand {
    position: absolute; left: 340px; width: 220px; top: 270px;
    text-align: center;
  }
  .front-brand__name {
    font: 400 28px/1 "Marcellus", serif;
    letter-spacing: 9px; margin-right: -9px;
    color: var(--cream);
  }
  .front-brand__since {
    margin-top: 8px;
    font: 700 8px/1 "Montserrat", sans-serif;
    letter-spacing: 5px; margin-right: -5px;
    color: var(--cream);
  }

  .back-brand { position: absolute; left: 0; right: 0; top: 148px; text-align: center; }
  .back-brand__name {
    font: 400 54px/1 "Marcellus", serif;
    letter-spacing: 18px; margin-right: -18px;
    color: var(--wordmark-gold);
  }
  .back-brand__since {
    margin-top: 14px;
    font: 800 15px/1 "Montserrat", sans-serif;
    letter-spacing: 11px; margin-right: -11px;
    color: var(--ink-soft);
  }
</style>
</head>
<body>
<div class="canvas">
  <section class="card card--front">
    <h1 class="company-name">KORBALT VANDRUP</h1>
    <p class="job-title">CEO &amp; Founder</p>
    <p class="person-name">Lars Henrik Vandrup</p>
    <ul class="contact-list">
      <li class="contact-item">
        <svg class="contact-icon" viewBox="0 0 24 24" aria-hidden="true"><path d="M6.6 10.8a15.1 15.1 0 0 0 6.6 6.6l2.2-2.2c.3-.3.7-.4 1-.2 1.1.4 2.3.6 3.6.6.6 0 1 .4 1 1V20c0 .6-.4 1-1 1A17 17 0 0 1 3 4c0-.6.4-1 1-1h3.5c.6 0 1 .4 1 1 0 1.2.2 2.4.6 3.6.1.3 0 .7-.2 1z"/></svg>
        004791 555 027
      </li>
      <li class="contact-item">
        <svg class="contact-icon" viewBox="0 0 24 24" aria-hidden="true"><path d="M2 5h20v14H2z M3.5 6.5 12 13l8.5-6.5" fill="none" stroke="currentColor"/><path d="M2 5h20v14H2zm2 2v.3l8 6 8-6V7l-8 6z"/></svg>
        korbalt.llc@mailbox.com
      </li>
      <li class="contact-item">
        <svg class="contact-icon" viewBox="0 0 24 24" aria-hidden="true"><path d="M12 2a10 10 0 1 0 0 20 10 10 0 0 0 0-20zm0 2c1 1.2 1.8 3 2.1 5H9.9C10.2 7 11 5.2 12 4zM4.3 9h3.6a17 17 0 0 0 0 6H4.3a8 8 0 0 1 0-6zm5.6 0h4.2a15 15 0 0 1 0 6H9.9a15 15 0 0 1 0-6zm6.2 0h3.6a8 8 0 0 1 0 6h-3.6a17 17 0 0 0 0-6zM9.9 17h4.2c-.3 2-1.1 3.8-2.1 5-1-1.2-1.8-3-2.1-5z"/></svg>
        www.korbalt.llc
      </li>
    </ul>
    <div class="front-brand">
      <div class="front-brand__name">KORBALT</div>
      <div class="front-brand__since">SINCE 2026</div>
    </div>
  </section>

  <section class="card card--back">
    <div class="back-brand">
      <div class="back-brand__name">KORBALT</div>
      <div class="back-brand__since">SINCE 2026</div>
    </div>
  </section>
</div>
</body>
</html>
```